Direct mail campaign for Quillmarsh Lien Services

Hello. We need a few design options for a direct mail campaign in the name of getting new clients. We are a lien processing company, www.quillmarshlien-example.com (the website is terrible and is in the process of redesign, so just pay attention to the content, not the design)

A "preliminary notice" is a legal document that we send on behalf of our customers. We aren't lawyers and this "notice" only becomes a legal document once the contractor isn't paid for his work. It's basically a document telling the owner or a property that you're working on the betterment of their property and expect to be paid for your work.

I plan on printing this document on something other than paper. I want it to stand out when it's in someone's hand. I haven't decided on what material and it shouldn't effect the design options, but just so you know I'm thinking of something very creative and different. Not a typical postcard.

Target Market(s)

Contractors and suppliers in the construction industry

Industry/Entity Type

Construction

Font styles to use
Serif

Requirements
Must have
• Dedicated and friendly customer service
• Simple and user friendly online interface
• No quotas
• No set-up fees

```html
<!DOCTYPE html>
<html lang="en">
<head>
<meta charset="utf-8">
<title>Quillmarsh Lien Services – Direct Mail Postcard</title>
<link href="https://fonts.googleapis.com/css2?family=Cormorant+Garamond:wght@500&family=Michroma&family=Orbitron:wght@700;900&family=Arimo:wght@400&family=Roboto+Condensed:ital,wght@0,700;1,400&family=Oswald:wght@700&family=Open+Sans:wght@400;600&display=swap" rel="stylesheet">
<style>
  :root {
    --bg: #e4e5e7;
    --blue: #2a86d1;
    --blue-deep: #1c64ad;
    --black: #1a1a1a;
    --white: #ffffff;
    --ink: #222222;
    --placeholder: #eeeeea;
  }
  html, body {
    margin: 0;
    padding: 0;
    width: 1200px;
    height: 1200px;
    overflow: hidden;
    background: var(--bg);
  }
  .canvas { position: relative; width: 1200px; height: 1200px; }
  .postcard { position: absolute; display: block; background: var(--white); }
  .postcard--front { left: 293px; top: 117px; width: 651px; height: 420px; }
  .postcard--back  { left: 284px; top: 717px; width: 668px; height: 431px; }

  .brand-name { font-family: "Cormorant Garamond", serif; font-weight: 500; fill: var(--ink); }
  .headline-kicker { font-family: "Michroma", sans-serif; fill: var(--ink); }
  .headline-main { font-family: "Arimo", sans-serif; fill: var(--blue); }
  .feature-text { font-family: "Roboto Condensed", sans-serif; font-weight: 700; fill: var(--white); }
  .contact-label, .contact-phone { font-family: "Open Sans", sans-serif; font-weight: 400; fill: var(--white); }
  .badge-no { font-family: "Orbitron", sans-serif; font-weight: 700; fill: var(--blue-deep); }
  .badge-word { font-family: "Oswald", sans-serif; font-weight: 700; fill: var(--black); }
  .badge-fees { font-family: "Orbitron", sans-serif; font-weight: 900; fill: var(--blue); }
  .welcome-title { font-family: "Orbitron", sans-serif; font-weight: 700; fill: var(--blue); }
  .welcome-sub { font-family: "Michroma", sans-serif; fill: var(--white); }
  .about-copy { font-family: "Roboto Condensed", sans-serif; font-style: italic; font-weight: 400; fill: var(--ink); }
  .footer-info { font-family: "Open Sans", sans-serif; font-weight: 600; fill: var(--white); }
</style>
</head>
<body>
<main class="canvas">

  <!-- Front of postcard -->
  <svg class="postcard postcard--front" viewBox="0 0 760 490" xmlns="http://www.w3.org/2000/svg">
    <defs>
      <linearGradient id="front-photo-tone" x1="0" y1="0" x2="1" y2="1">
        <stop offset="0" stop-color="#f2f5f9"/>
        <stop offset="0.55" stop-color="#c9d9ea"/>
        <stop offset="1" stop-color="#5f93c9"/>
      </linearGradient>
      <linearGradient id="band-blue" x1="0" y1="0" x2="1" y2="0">
        <stop offset="0" stop-color="#1f6fbb"/>
        <stop offset="1" stop-color="#3a97dc"/>
      </linearGradient>
      <linearGradient id="panel-black" x1="0" y1="0" x2="1" y2="1">
        <stop offset="0" stop-color="#2b2b2b"/>
        <stop offset="1" stop-color="#0e0e0e"/>
      </linearGradient>
      <linearGradient id="badge-face" x1="0" y1="0" x2="0" y2="1">
        <stop offset="0" stop-color="#ffffff"/>
        <stop offset="1" stop-color="#e3e6ea"/>
      </linearGradient>
    </defs>

    <rect class="card-base" width="760" height="490" fill="var(--white)"/>

    <polygon class="photo-frame-black" points="298,0 352,0 404,318 380,322" fill="var(--black)"/>
    <polygon class="photo-frame-blue" points="340,0 358,0 408,318 396,320" fill="var(--blue)"/>
    <polygon class="photo-area" role="img" aria-label="Photo: hands with a pencil and calculator reviewing sales charts" points="356,0 760,0 760,285 406,322" fill="url(#front-photo-tone)"/>

    <text class="brand-name" x="150" y="62" font-size="19" text-anchor="middle" textLength="236" lengthAdjust="spacing">QUILLMARSH LIEN SERVICES</text>

    <polygon class="logo-rule-black" points="0,92 300,110 302,114 0,95" fill="var(--black)"/>
    <polygon class="logo-rule-blue" points="0,97 338,120 340,136" fill="var(--blue)"/>

    <text class="headline-kicker" x="32" y="168" font-size="16" textLength="282">EXPECT TO BE PAID</text>
    <text class="headline-main" x="30" y="198" font-size="31" textLength="286">FOR YOUR WORK</text>

    <polygon class="feature-bar-edge" points="0,218 348,218 364,262 0,262" fill="var(--black)"/>
    <polygon class="feature-bar" points="0,220 345,220 358,258 0,258" fill="url(#band-blue)"/>
    <text class="feature-text" x="22" y="247" font-size="17" textLength="303">Dedicated and friendly customer service</text>

    <polygon class="feature-bar-edge" points="0,273 382,273 398,317 0,317" fill="var(--black)"/>
    <polygon class="feature-bar" points="0,275 379,275 392,313 0,313" fill="url(#band-blue)"/>
    <text class="feature-text" x="22" y="302" font-size="17" textLength="308">Simple and user friendly online interface</text>

    <polygon class="base-band" points="0,490 0,488 380,388 760,292 760,490" fill="url(#band-blue)"/>
    <polygon class="contact-panel" points="0,317 398,317 400,384 0,484" fill="url(#panel-black)"/>
    <polygon class="contact-panel-rule" points="0,484 400,384 402,390 0,490" fill="var(--white)"/>

    <text class="contact-label" x="31" y="359" font-size="25">Contact Us</text>
    <rect class="contact-rule" x="178" y="350" width="75" height="3" fill="var(--white)"/>
    <text class="contact-phone" x="30" y="400" font-size="34" textLength="238">555-214-0187</text>

    <!-- badge: no estimate -->
    <polygon points="448,294 524.2,338 524.2,426 448,470 371.8,426 371.8,338" fill="var(--white)"/>
    <polygon points="448,299 519.9,340.5 519.9,423.5 448,465 376.1,423.5 376.1,340.5" fill="var(--blue)"/>
    <polygon points="448,309 511.2,345.5 511.2,418.5 448,455 384.8,418.5 384.8,345.5" fill="url(#badge-face)"/>
    <text class="badge-no" x="448" y="382" font-size="36" text-anchor="middle" textLength="96">NO</text>
    <text class="badge-word" x="448" y="420" font-size="34" text-anchor="middle" textLength="112" lengthAdjust="spacingAndGlyphs">ESTIMATE</text>

    <!-- badge: no set-up fees -->
    <polygon points="645,262 729.9,311 729.9,409 645,458 560.1,409 560.1,311" fill="var(--white)"/>
    <polygon points="645,268 724.7,314 724.7,406 645,452 565.3,406 565.3,314" fill="var(--blue)"/>
    <polygon points="645,279 715.1,319.5 715.1,400.5 645,441 574.9,400.5 574.9,319.5" fill="url(#badge-face)"/>
    <text class="badge-no" x="645" y="338" font-size="36" text-anchor="middle" textLength="96">NO</text>
    <text class="badge-word" x="645" y="378" font-size="40" text-anchor="middle" textLength="102" lengthAdjust="spacingAndGlyphs">SET-UP</text>
    <text class="badge-fees" x="645" y="414" font-size="30" text-anchor="middle" textLength="104" lengthAdjust="spacingAndGlyphs">FEES</text>
  </svg>

  <!-- Back of postcard -->
  <svg class="postcard postcard--back" viewBox="0 0 779 503" xmlns="http://www.w3.org/2000/svg">
    <defs>
      <linearGradient id="back-photo-tone" x1="0" y1="0" x2="1" y2="1">
        <stop offset="0" stop-color="#e6eef6"/>
        <stop offset="0.5" stop-color="#8fb2d8"/>
        <stop offset="1" stop-color="#2a5f9f"/>
      </linearGradient>
      <linearGradient id="back-band-blue" x1="0" y1="0" x2="1" y2="0">
        <stop offset="0" stop-color="#1f6fbb"/>
        <stop offset="1" stop-color="#3a97dc"/>
      </linearGradient>
      <linearGradient id="copy-panel" x1="0" y1="0" x2="1" y2="0">
        <stop offset="0" stop-color="#f4f4f4"/>
        <stop offset="1" stop-color="#dcdcdc"/>
      </linearGradient>
      <linearGradient id="back-badge-face" x1="0" y1="0" x2="0" y2="1">
        <stop offset="0" stop-color="#ffffff"/>
        <stop offset="1" stop-color="#e3e6ea"/>
      </linearGradient>
    </defs>

    <rect class="card-base" width="779" height="503" fill="var(--white)"/>

    <polygon class="photo-area" role="img" aria-label="Photo: stacks of coins over financial documents in blue light" points="0,0 325,0 312,146 0,232" fill="url(#back-photo-tone)"/>

    <polygon class="edge-stripe" points="325,0 345,0 462,418 436,418" fill="var(--black)"/>

    <polygon class="welcome-panel" points="0,242 306,158 336,293 0,293" fill="var(--black)"/>
    <text class="welcome-title" x="28" y="262" font-size="23" textLength="248" lengthAdjust="spacing">WELCOME TO</text>
    <text class="welcome-sub" x="28" y="281" font-size="11" textLength="254" lengthAdjust="spacingAndGlyphs">QUILLMARSH LIEN SERVICES, INC.</text>

    <polygon class="copy-panel" points="0,293 338,293 362,418 0,418" fill="url(#copy-panel)"/>
    <text class="about-copy" font-size="10.8">
      <tspan x="28" y="320" textLength="334" lengthAdjust="spacing">We specialize in preparing Arizona 20-Day Preliminary Notices (prelien) &amp;</tspan>
      <tspan x="28" y="334" textLength="334" lengthAdjust="spacing">Mechanic's Liens. We prepare and send via certified and certificate of</tspan>
      <tspan x="28" y="348" textLength="334" lengthAdjust="spacing">mail-ing your Preliminary Notices (preliens) for job sites anywhere within</tspan>
      <tspan x="28" y="362" textLength="334" lengthAdjust="spacing">the continental United States. as well as perfecting liens and filing them for</tspan>
      <tspan x="28" y="376" textLength="334" lengthAdjust="spacing">you at the appropriate County Recorder's Office. We also give Bonding</tspan>
      <tspan x="28" y="390" textLength="334" lengthAdjust="spacing">Notice for city. county. and military jobs. We are established here in Harlow.</tspan>
      <tspan x="28" y="404">for your convenience.</tspan>
    </text>

    <polygon class="footer-stripe" points="362,418 462,418 392,503 340,503" fill="var(--black)"/>
    <polygon class="footer-band" points="0,418 414,418 340,503 0,503" fill="url(#back-band-blue)"/>

    <g class="icon-pin" fill="var(--white)">
      <circle cx="25" cy="437" r="3.6"/>
      <polygon points="21.6,438.5 28.4,438.5 25,445"/>
      <circle cx="25" cy="437" r="1.3" fill="#2575c2"/>
    </g>
    <text class="footer-info" font-size="11">
      <tspan x="33" y="444">Quillmarsh Lien Services</tspan>
      <tspan x="33" y="459">PO Box 40117 Harlow,</tspan>
      <tspan x="33" y="474">Az 85990</tspan>
    </text>

    <path class="icon-phone" d="M175,436 q1.5,-1.5 3,0 l1.2,1.6 q0.6,1 -0.4,1.8 q0.8,2 2.6,2.8 q0.8,-1 1.8,-0.4 l1.6,1.2 q1.5,1.5 0,3 q-3,1.5 -7,-2.5 q-4,-4 -2.8,-7.5z" fill="var(--white)"/>
    <g class="icon-fax" fill="var(--white)">
      <rect x="175" y="453" width="9" height="3.5" rx="0.8"/>
      <rect x="176.5" y="456.5" width="6" height="4"/>
    </g>
    <g class="icon-globe" fill="none" stroke="var(--white)" stroke-width="1.1">
      <circle cx="179.5" cy="470" r="4.2"/>
      <ellipse cx="179.5" cy="470" rx="1.8" ry="4.2"/>
      <line x1="175.3" y1="470" x2="183.7" y2="470"/>
    </g>
    <text class="footer-info" font-size="11">
      <tspan x="187" y="444">555.214.0187</tspan>
      <tspan x="187" y="459">555.214.0199</tspan>
      <tspan x="187" y="474">www.quillmarshlien-example.com</tspan>
    </text>

    <polygon points="380,98 466.6,148 466.6,248 380,298 293.4,248 293.4,148" fill="var(--white)"/>
    <polygon points="380,104 461.4,151 461.4,245 380,292 298.6,245 298.6,151" fill="var(--blue-deep)"/>
    <polygon points="380,115 451.9,156.5 451.9,239.5 380,281 308.1,239.5 308.1,156.5" fill="url(#back-badge-face)"/>
    <text class="badge-no" x="380" y="172" font-size="40" text-anchor="middle" textLength="100">NO</text>
    <text class="badge-word" x="380" y="216" font-size="44" text-anchor="middle" textLength="106" lengthAdjust="spacingAndGlyphs">SET-UP</text>
    <text class="badge-fees" x="380" y="253" font-size="31" text-anchor="middle" textLength="108" lengthAdjust="spacingAndGlyphs">FEES</text>

    <text class="brand-name" x="520" y="60" font-size="17" text-anchor="middle" textLength="200" lengthAdjust="spacing">QUILLMARSH LIEN SERVICES</text>

    <rect class="stamp-box" x="670" y="26" width="86" height="85" fill="var(--placeholder)"/>
    <rect class="address-box" x="503" y="260" width="249" height="115" fill="var(--placeholder)"/>
  </svg>

</main>
</body>
</html>
```